Velora Studio business site requires luxurious wix template design

I need a wix web template design that will deliver a consistent look and feel across mobile and computer access. Designs should follow the boudoir theme, be classy, and luxurious looking. Gold or silver inlay, velvet feel.
The majority of my clients will be women from the age of 22-40, and will be interested in boosting their self-esteem, feeling feminine, romance etc. They may want a shoot to celebrate a pending wedding, or a fitness achievement.

Target Market(s)

Females between 22-40 years of age

Logo Text

Velora Studio Canada (or Velora Studio)

Font styles to use
Decorative
Script

Colors

Designer to choose colors to be used in the design.

Requirements
Must have
• Site will have booking component for appointments, merchandise may be made available (photos, books)

```html
<!DOCTYPE html>
<html lang="en">
<head>
<meta charset="utf-8">
<title>Velora Studio</title>
<link href="https://fonts.googleapis.com/css2?family=Arimo:wght@400;700&display=swap" rel="stylesheet">
<style>
:root{
  --gold:#f5c400;
  --ink:#111111;
  --white:#ffffff;
  --velvet:#5e1616;
  --velvet-dark:#3a0a0a;
  --line:#c9c9c9;
  --footer:#000000;
  --muted:#9a9a9a;
}
*{box-sizing:border-box;margin:0;padding:0}
html,body{width:1200px;height:4276px;overflow:hidden}
body{font-family:"Arimo",Arial,sans-serif;color:var(--ink);background:var(--white);position:relative}
.abs{position:absolute}

/* header */
.site-header{left:0;top:0;width:1200px;height:250px;background:var(--white)}
.brand{display:flex;align-items:center;gap:24px;position:absolute;left:0;right:0;top:54px;justify-content:center}
.brand-mark{width:62px;height:62px;border:5px solid var(--ink);border-radius:50%;display:block}
.brand-name{font-size:39px;font-weight:700}
.main-nav{position:absolute;left:0;right:0;top:166px;display:flex;justify-content:center;gap:16px;font-size:17px;font-weight:700}
.nav-item{color:var(--ink);padding:8px 15px;border:3px solid transparent}
.nav-item.is-active{border-color:var(--gold)}

/* hero */
.hero{left:0;top:250px;width:1200px;height:585px;
  background:
    radial-gradient(ellipse 30% 45% at 55% 55%,rgba(238,232,224,.55),transparent 70%),
    radial-gradient(ellipse 25% 40% at 85% 40%,rgba(60,55,50,.6),transparent 70%),
    linear-gradient(135deg,#5f564d 0%,#9e8f80 35%,#c5b8a8 55%,#8c7f72 75%,#3f3a35 100%)}
.hero-social{left:90px;top:177px;display:flex;flex-direction:column;gap:15px}
.hero-social span{width:32px;height:32px;border:2px solid var(--white);border-radius:50%;display:block}
.hero-dots{right:58px;top:250px;display:flex;flex-direction:column;gap:10px}
.hero-dots span{width:7px;height:7px;border-radius:50%;background:var(--white);display:block}
.hero-title{left:0;right:0;top:188px;text-align:center;color:var(--white);font-size:55px;font-weight:700;line-height:68px;text-shadow:0 2px 6px rgba(0,0,0,.35)}
.hero-sub{left:0;right:0;top:336px;display:flex;justify-content:center;align-items:center;gap:18px;color:var(--white);font-size:17px;letter-spacing:.5px}
.hero-sub i{display:block;width:130px;height:1px;background:var(--white)}
.btn{display:flex;align-items:center;justify-content:center;border:4px solid var(--gold);border-radius:31px;font-size:20px;color:var(--white)}
.hero .btn{left:508px;top:398px;width:184px;height:60px}

/* about */
.about-photo{left:0;top:835px;width:572px;height:490px;
  background:radial-gradient(ellipse 40% 50% at 60% 50%,#d6b39a,transparent 75%),linear-gradient(160deg,#9fbd85 0%,#c9ad8f 50%,#7a5a47 100%)}
.about-title{left:622px;top:888px;font-size:39px;font-weight:700}
.about-title em{font-style:normal;color:var(--gold)}
.about-text{left:622px;top:978px;width:455px;font-size:17px;line-height:27px}
.btn-book{left:622px;top:1230px;width:184px;height:60px;color:var(--ink);font-size:18px}

/* gallery */
.gallery{left:0;top:1325px;width:1200px;height:1210px;display:grid;grid-template-columns:400px 400px 400px;grid-template-rows:404px 403px 403px}
.gallery div{width:100%;height:100%}
.g1{background:radial-gradient(ellipse at 50% 45%,#c8a890,transparent 65%),linear-gradient(135deg,#6e5f55,#a99888)}
.g2{background:radial-gradient(ellipse at 50% 50%,#b89a82,transparent 60%),linear-gradient(135deg,#d0cbc3,#928679)}
.g3{background:radial-gradient(ellipse at 55% 45%,#e9c9b3,transparent 60%),linear-gradient(135deg,#d5e7f1,#8fb4cc)}
.g4{background:radial-gradient(ellipse at 45% 55%,#f2cfc0,transparent 60%),linear-gradient(135deg,#e5336a,#f0a6a6)}
.g5{background:radial-gradient(ellipse at 50% 55%,#f0d6c4,transparent 60%),linear-gradient(135deg,#e8d8cc,#c8703f)}
.g6{background:radial-gradient(ellipse at 50% 60%,#5a4a40,transparent 60%),linear-gradient(135deg,#eef2f5,#9a9088)}
.g7{background:radial-gradient(ellipse at 60% 75%,#f0d4d8,transparent 55%),linear-gradient(135deg,#355f24,#b9c79a)}
.g8{background:radial-gradient(ellipse at 50% 50%,#d8b49a,transparent 60%),linear-gradient(135deg,#e4d3bf,#5e4e42)}
.g9{background:radial-gradient(ellipse at 55% 45%,#d9c4b6,transparent 60%),linear-gradient(135deg,#9d958e,#cfc4bb)}

/* merchandise */
.merch{left:0;top:2535px;width:1200px;height:490px;
  background:radial-gradient(ellipse 70% 80% at 50% 40%,var(--velvet) 0%,var(--velvet-dark) 100%)}
.merch-title{left:0;right:0;top:82px;text-align:center;color:var(--gold);font-size:38px;font-weight:700}
.merch-text{left:232px;width:736px;top:170px;text-align:center;color:var(--white);font-size:17px;line-height:28px}
.merch .btn{left:518px;top:358px;width:184px;height:60px}

/* booking */
.booking{left:0;top:3025px;width:1200px;height:740px;background:var(--white)}
.book-title{left:120px;top:137px;font-size:39px;font-weight:700}
.book-contact{left:120px;top:212px;font-size:16px;line-height:21px;font-style:normal}
.field{left:115px;width:377px;height:40px;border:1px solid var(--line);font-size:13px;color:var(--muted);padding:11px 10px}
.f1{top:342px}.f2{top:397px}.f3{top:452px}
.f4{top:518px;height:112px}
.btn-send{left:218px;top:660px;width:142px;height:48px;color:var(--ink);font-size:20px}
.book-photo{left:598px;top:0;width:602px;height:740px;
  background:radial-gradient(ellipse 45% 40% at 55% 45%,#e7c7b2,transparent 70%),linear-gradient(150deg,#6e5040 0%,#c9a38c 45%,#f2e7df 100%)}

/* footer */
.site-footer{left:0;top:3765px;width:1200px;height:511px;background:var(--footer);color:var(--white)}
.foot-brand{left:115px;top:112px;display:flex;align-items:center;gap:26px}
.foot-brand .brand-mark{border-color:var(--white)}
.foot-brand .brand-name{font-size:36px}
.foot-text{left:115px;top:218px;width:455px;font-size:17px;line-height:27px}
.foot-links{left:722px;top:122px}
.foot-head{font-size:18px;font-weight:700;margin-bottom:14px}
.foot-links ul{list-style:none;font-size:16px;line-height:26px}
.newsletter{left:917px;top:122px;width:220px}
.newsletter p{font-size:15px;line-height:24px;margin-bottom:20px}
.news-input{width:196px;height:34px;background:var(--white);border-radius:3px;color:#444;font-size:12px;padding:10px 6px}
.news-btn{margin:14px 0 0 60px;width:80px;height:30px;border-radius:4px;background:#d9d9d9;color:#555;font-size:14px;display:flex;align-items:center;justify-content:center}
.copyright{left:0;right:0;top:458px;text-align:center;font-size:16px}
</style>
</head>
<body>

<header class="site-header abs">
  <div class="brand"><span class="brand-mark"></span><span class="brand-name">Velora Studio</span></div>
  <nav class="main-nav">
    <span class="nav-item is-active">Home</span><span class="nav-item">About</span><span class="nav-item">Portfolio</span><span class="nav-item">Contact</span><span class="nav-item">Shop</span><span class="nav-item">Book Online</span>
  </nav>
</header>

<section class="hero abs" role="img" aria-label="Wedding party celebrating outdoors as petals are thrown over a bride and groom">
  <div class="hero-social abs"><span></span><span></span><span></span><span></span></div>
  <div class="hero-dots abs"><span></span><span></span><span></span></div>
  <h1 class="hero-title abs">WELCOME TO VELORA<br>STUDIO</h1>
  <div class="hero-sub abs"><i></i>WEDDING PHOTOGRAPHY<i></i></div>
  <span class="btn abs">View More</span>
</section>

<section class="about">
  <div class="about-photo abs" role="img" aria-label="Smiling photographer in a straw hat holding a camera"></div>
  <h2 class="about-title abs"><em>About</em> me</h2>
  <p class="about-text abs">Lorem Ipsum is simply dummy text of the printing and typesetting industry. Lorem Ipsum has been the industry's standard dummy text ever since the 1500s, when an unknown printer took a galley of type and scrambled it to make a type specimen book. It has survived not only five centuries, but also the leap into electronic typesetting, remaining essentially unchanged.</p>
  <span class="btn btn-book abs">Book A Session</span>
</section>

<section class="gallery abs" aria-label="Portfolio">
  <div class="g1" role="img" aria-label="Confident woman with arms crossed"></div>
  <div class="g2" role="img" aria-label="Woman flexing her arms after a fitness achievement"></div>
  <div class="g3" role="img" aria-label="Joyful woman celebrating"></div>
  <div class="g4" role="img" aria-label="Woman reaching toward the camera on a pink backdrop"></div>
  <div class="g5" role="img" aria-label="Excited red-haired woman framing her face with her hands"></div>
  <div class="g6" role="img" aria-label="Woman hugging her dog in the snow"></div>
  <div class="g7" role="img" aria-label="Bride and groom with a bouquet"></div>
  <div class="g8" role="img" aria-label="Couple sharing a kiss on the cheek"></div>
  <div class="g9" role="img" aria-label="Hand showing an engagement ring"></div>
</section>

<section class="merch abs">
  <h2 class="merch-title abs">Merchandise</h2>
  <p class="merch-text abs">Lorem Ipsum is simply dummy text of the printing and typesetting industry. Lorem Ipsum has been the industry's standard dummy text ever since the 1500s, when an unknown printer took a galley of type and scrambled it to make a type specimen book. It has survived not only five centuries, but also the leap into electronic typesetting, remaining essentially unchanged.</p>
  <span class="btn abs">Shop More</span>
</section>

<section class="booking abs">
  <h2 class="book-title abs">Book Appointments</h2>
  <address class="book-contact abs">218 Maple Crest Ave.<br>Halton, ON L7R 2K4<br>Tel: 555-014-2287<br>hello@velorastudio.ca</address>
  <div class="field f1 abs">Name</div>
  <div class="field f2 abs">Email</div>
  <div class="field f3 abs">Appointments</div>
  <div class="field f4 abs">Message</div>
  <span class="btn btn-send abs">Send</span>
  <div class="book-photo abs" role="img" aria-label="Soft portrait of a bride leaning on her partner"></div>
</section>

<footer class="site-footer abs">
  <div class="foot-brand abs"><span class="brand-mark"></span><span class="brand-name">Velora Studio</span></div>
  <p class="foot-text abs">Lorem Ipsum is simply dummy text of the printing and typesetting industry. Lorem Ipsum has been the industry's standard dummy text ever since the 1500s, when an unknown printer took a galley of type and scrambled it to make a type specimen book.</p>
  <div class="foot-links abs">
    <div class="foot-head">LINK</div>
    <ul><li>Home</li><li>About</li><li>Portfolio</li><li>Contact</li><li>Shop</li><li>Book Online</li></ul>
  </div>
  <div class="newsletter abs">
    <div class="foot-head">NEWSLETTER</div>
    <p>Register your email for news for Photography</p>
    <div class="news-input">Enter the email</div>
    <div class="news-btn">Submit</div>
  </div>
  <div class="copyright abs">© Velora Studio.All Rights Reserved.</div>
</footer>

</body>
</html>
```